Business cards for Harbourline Supply Pty Ltd that import building products into Australia from China
Target Market(s)
Business to Business
Industry/Entity Type
Business
Contact Information for Business Card
Front: Logo and Business Name
Rear:
Vernon Asquill
General Manager
Mobile: 0427 196 354
email: vern@harbourlinesupply.com.au
alternative email: vern@ochrefield.com.au
web: www.harbourlinesupply.com.au
Carrow, Brindlemere and Tallis
Colors
ec1f27
fbee3d

```html
<!DOCTYPE html>
<html lang="en">
<head>
<meta charset="utf-8">
<title>Harbourline Supply Pty Ltd — Business Cards</title>
<link rel="stylesheet" href="https://fonts.googleapis.com/css2?family=Exo+2:wght@400;500;700&display=swap">
<style>
  :root {
    --stage: #b8b8b8;
    --card-light: #ffffff;
    --card-dark: #1c1c1c;
    --brand-red: #ec1f27;
    --brand-yellow: #fbee3d;
    --ink: #1e1e1e;
    --ink-soft: #2a2a2a;
    --mark-light: #ececec;
    --rule: #d9b9bf;
  }
  * { box-sizing: border-box; margin: 0; padding: 0; }
  html, body { width: 1200px; height: 900px; overflow: hidden; }
  body {
    background: var(--stage);
    font-family: "Exo 2", sans-serif;
    position: relative;
  }
  .card {
    position: absolute;
    top: 184px;
    height: 491px;
    border-radius: 14px;
    box-shadow: 3px 4px 6px rgba(0,0,0,0.28);
  }
  .card--details { left: 299px; width: 301px; background: var(--card-light); }
  .card--brand { left: 645px; width: 305px; background: var(--card-dark); }

  .wordmark {
    position: absolute;
    left: 0; right: 0;
    display: flex;
    flex-direction: column;
    align-items: center;
  }
  .wordmark__square {
    width: 58px; height: 58px;
    background: var(--brand-red);
    margin-bottom: 14px;
  }
  .wordmark__name {
    font-weight: 700;
    font-size: 26px;
    line-height: 1.05;
    text-align: center;
  }
  .card--details .wordmark { top: 40px; }
  .card--details .wordmark__name { color: var(--ink); }
  .card--brand .wordmark { top: 170px; }
  .card--brand .wordmark__name { color: var(--mark-light); }

  .contact {
    position: absolute;
    left: 32px;
    top: 256px;
    right: 33px;
    color: var(--ink-soft);
  }
  .contact__name {
    font-weight: 700;
    font-size: 21px;
    letter-spacing: 0.3px;
    line-height: 24px;
    color: var(--ink);
  }
  .contact__name .given { color: var(--brand-red); }
  .contact__role {
    font-weight: 500;
    font-size: 13.5px;
    margin-top: 2px;
  }
  .contact__list {
    list-style: none;
    margin-top: 14px;
  }
  .contact__list li {
    display: flex;
    align-items: center;
    height: 22px;
    font-size: 14px;
  }
  .contact__list svg {
    width: 12px; height: 12px;
    margin-right: 9px;
    fill: var(--brand-red);
    flex: none;
  }
  .contact__rule {
    border: 0;
    border-top: 1px solid var(--rule);
    margin-top: 10px;
  }
  .contact__offices {
    font-size: 14px;
    margin-top: 12px;
  }
</style>
</head>
<body>
  <section class="card card--details">
    <div class="wordmark">
      <span class="wordmark__square"></span>
      <span class="wordmark__name">Harbourline Supply<br>Pty Ltd</span>
    </div>
    <div class="contact">
      <h1 class="contact__name"><span class="given">VERNON</span> ASQUILL</h1>
      <p class="contact__role">General Manager</p>
      <ul class="contact__list">
        <li>
          <svg viewBox="0 0 12 12" aria-hidden="true"><path d="M1 4.2C1 2.6 3 1.5 6 1.5s5 1.1 5 2.7v1H8.6V4H3.4v1.2H1zM3 5.6h6l1.6 4.9H1.4z"/></svg>
          0427 196 354
        </li>
        <li>
          <svg viewBox="0 0 12 12" aria-hidden="true"><path d="M1 2.5h10v7H1z M1.6 3.2 6 6.6l4.4-3.4" stroke="#fff" stroke-width="0.9"/></svg>
          vern@harbourlinesupply.com.au
        </li>
        <li>
          <svg viewBox="0 0 12 12" aria-hidden="true"><path d="M1 2.5h10v7H1z M1.6 3.2 6 6.6l4.4-3.4" stroke="#fff" stroke-width="0.9"/></svg>
          vern@ochrefield.com.au
        </li>
        <li>
          <svg viewBox="0 0 12 12" aria-hidden="true"><circle cx="6" cy="6" r="5.2"/><path d="M3 3.5c1 .3 1.4 1 1.2 1.8-.2.8.6 1.2 1.3 1.4.5.6 0 1.6-.4 2.3M7 2c.2.8 1 1 1.8.9.5.7.3 1.5-.3 2" stroke="#fff" stroke-width="0.8" fill="none"/></svg>
          www.harbourlinesupply.com.au
        </li>
      </ul>
      <hr class="contact__rule">
      <p class="contact__offices">Carrow, Brindlemere and Tallis</p>
    </div>
  </section>

  <section class="card card--brand">
    <div class="wordmark">
      <span class="wordmark__square"></span>
      <span class="wordmark__name">Harbourline Supply<br>Pty Ltd</span>
    </div>
  </section>
</body>
</html>
```